Wine Label: Tressivo

The project is to create 3 wine labels. The brand name is "Tressivo"

What we need is to have 3 versions: red wine, white wine and rose.

The wine is for young and modern people, between 21 and 31 years old, so it need to be casual, modern and fun, but at the same time it needs to keep the Premiums of a good European wine.

It is from Italy.

Target Market(s)

Young adults, between 21 and 31 years old. wine lovers

Requirements
Must have
• - Modern colors (Black, silver, red, etc.)
• - Clean label
• - Clear font
• - Style
• - The brand + the type of wine (red, white or rose)
Nice to have
• - A symbol to represent the brand
Should not have
• - Many elements
• - No clear fonts
• - No funny colors

```html
<!DOCTYPE html>
<html lang="en">
<head>
<meta charset="utf-8">
<title>Tressivo – Wine Label Set</title>
<link rel="stylesheet" href="https://fonts.googleapis.com/css2?family=Josefin+Sans:wght@300;400&family=Oswald:wght@200&family=Pinyon+Script&display=swap">
<style>
  :root {
    --page: #ffffff;
    --ink: #111111;
    --label: #000000;
    --brand: #f2f2f2;
    --tagline: #bdbdbd;
    --white-wine: #e6e6e6;
    --rose-wine: #c99ac4;
    --red-wine: #d3141c;
  }

  html, body {
    margin: 0;
    padding: 0;
    width: 1200px;
    height: 900px;
    overflow: hidden;
    background: var(--page);
  }

  .sheet {
    position: relative;
    width: 1200px;
    height: 900px;
    background: var(--page);
    font-family: "Josefin Sans", sans-serif;
  }

  .section-title {
    position: absolute;
    margin: 0;
    font-family: "Josefin Sans", sans-serif;
    font-weight: 400;
    font-size: 28px;
    letter-spacing: 2.5px;
    color: var(--ink);
    white-space: nowrap;
  }
  .section-title--neck { left: 117px; top: 22px; }
  .section-title--main { left: 806px; top: 4px; }

  .label {
    position: absolute;
    background: var(--label);
    overflow: hidden;
  }

  .brand-name {
    display: block;
    font-family: "Oswald", sans-serif;
    font-weight: 200;
    color: var(--brand);
    text-transform: uppercase;
    line-height: 1;
    white-space: nowrap;
  }

  .tagline {
    display: block;
    margin-top: 2px;
    font-family: "Pinyon Script", cursive;
    font-size: 14px;
    line-height: 1;
    color: var(--tagline);
    white-space: nowrap;
  }

  .brand-dot {
    position: absolute;
    left: 50%;
    transform: translateX(-50%);
  }

  /* Bottleneck labels */
  .neck-label--white { left: 87px; top: 83px; width: 386px; height: 225px; --wine: var(--white-wine); }
  .neck-label--rose  { left: 81px; top: 373px; width: 391px; height: 228px; --wine: var(--rose-wine); }
  .neck-label--red   { left: 82px; top: 660px; width: 390px; height: 227px; --wine: var(--red-wine); }

  .neck-label__lockup {
    position: absolute;
    left: 50%;
    top: 78px;
    width: 130px;
    transform: translate(-50%, -50%) rotate(-90deg);
    text-align: center;
  }
  .neck-label .brand-name { font-size: 32px; letter-spacing: 0.5px; }
  .neck-label .brand-dot { top: 150px; width: 44px; height: 44px; margin-left: -2px; }

  /* Main labels */
  .main-label--white { left: 733px; top: 39px; width: 363px; height: 272px; --wine: var(--white-wine); }
  .main-label--rose  { left: 733px; top: 329px; width: 364px; height: 273px; --wine: var(--rose-wine); }
  .main-label--red   { left: 734px; top: 616px; width: 363px; height: 271px; --wine: var(--red-wine); }

  .main-label .brand-name {
    position: absolute;
    left: 0;
    right: 0;
    top: 20px;
    text-align: center;
    font-size: 38px;
    letter-spacing: 0.5px;
  }
  .main-label .brand-dot { top: 66px; width: 20px; height: 20px; }

  .wine-type {
    position: absolute;
    left: 0;
    right: 0;
    top: 120px;
    margin: 0;
    text-align: center;
    font-family: "Pinyon Script", cursive;
    font-weight: 400;
    font-size: 33px;
    line-height: 1.2;
    color: var(--wine);
  }
  .main-label--white .wine-type { color: #ffffff; }
</style>
</head>
<body>
<main class="sheet">
  <h2 class="section-title section-title--neck">BOTTLENECK LABELS</h2>
  <h2 class="section-title section-title--main">MAIN LABELS</h2>

  <section class="label neck-label neck-label--white" aria-label="Tressivo White bottleneck label">
    <div class="neck-label__lockup">
      <span class="brand-name">Tressivo</span>
      <span class="tagline">Finest Wine of Italy</span>
    </div>
    <svg class="brand-dot" viewBox="0 0 44 44" aria-hidden="true"><circle cx="22" cy="22" r="19" fill="none" stroke="var(--wine)" stroke-width="3"/></svg>
  </section>

  <section class="label neck-label neck-label--rose" aria-label="Tressivo Rosé bottleneck label">
    <div class="neck-label__lockup">
      <span class="brand-name">Tressivo</span>
      <span class="tagline">Finest Wine of Italy</span>
    </div>
    <svg class="brand-dot" viewBox="0 0 44 44" aria-hidden="true"><circle cx="22" cy="22" r="19" fill="none" stroke="var(--wine)" stroke-width="3"/></svg>
  </section>

  <section class="label neck-label neck-label--red" aria-label="Tressivo Red bottleneck label">
    <div class="neck-label__lockup">
      <span class="brand-name">Tressivo</span>
      <span class="tagline">Finest Wine of Italy</span>
    </div>
    <svg class="brand-dot" viewBox="0 0 44 44" aria-hidden="true"><circle cx="22" cy="22" r="19" fill="none" stroke="var(--wine)" stroke-width="3"/></svg>
  </section>

  <section class="label main-label main-label--white" aria-label="Tressivo White main label">
    <span class="brand-name">Tressivo</span>
    <svg class="brand-dot" viewBox="0 0 20 20" aria-hidden="true"><circle cx="10" cy="10" r="8" fill="none" stroke="var(--wine)" stroke-width="2"/></svg>
    <p class="wine-type">White</p>
  </section>

  <section class="label main-label main-label--rose" aria-label="Tressivo Rosé main label">
    <span class="brand-name">Tressivo</span>
    <svg class="brand-dot" viewBox="0 0 20 20" aria-hidden="true"><circle cx="10" cy="10" r="8" fill="none" stroke="var(--wine)" stroke-width="2"/></svg>
    <p class="wine-type">Rosé</p>
  </section>

  <section class="label main-label main-label--red" aria-label="Tressivo Red main label">
    <span class="brand-name">Tressivo</span>
    <svg class="brand-dot" viewBox="0 0 20 20" aria-hidden="true"><circle cx="10" cy="10" r="8" fill="none" stroke="var(--wine)" stroke-width="2"/></svg>
    <p class="wine-type">Red</p>
  </section>
</main>
</body>
</html>
```